I need a full PowerPoint template (with multiple slide options) for a new imaging center company - Brightwell Medical Imaging. I have attached the Logo and Brand Identity here.

```html
<!DOCTYPE html>
<html lang="en">
<head>
<meta charset="utf-8">
<title>Brightwell Medical Imaging – Presentation Template</title>
<link href="https://fonts.googleapis.com/css2?family=Montserrat:wght@400;500;600;700;800&display=swap" rel="stylesheet">
<style>
:root{
  --navy:#2b2d6e;
  --navy-dark:#1f2157;
  --green:#3cb44b;
  --blue:#2f7fc1;
  --sky:#e9f1f8;
  --pill:#eceef6;
  --text:#55586b;
  --page:#e6e8ee;
  --white:#ffffff;
}
*{margin:0;padding:0;box-sizing:border-box}
html,body{width:826px;height:1200px;overflow:hidden}
body{background:var(--page);font-family:'Montserrat',sans-serif;color:var(--text);position:relative}
.slide{position:absolute;width:400px;height:225px;background:var(--white);overflow:hidden;box-shadow:0 1px 4px rgba(30,35,80,.15)}
.col-a{left:12px}.col-b{left:414px}
.row-1{top:12px}.row-2{top:243px}.row-3{top:474px}.row-4{top:705px}.row-5{top:936px}
.abs{position:absolute}
.title{position:absolute;left:16px;top:14px;font-weight:800;font-size:13px;color:var(--navy);letter-spacing:.3px}
.body-copy{font-size:5.5px;line-height:1.55;color:var(--text)}
.footer{position:absolute;left:0;right:0;bottom:0;height:22px;border-top:1px solid #e4e6ee;display:flex;align-items:center;padding:0 14px;gap:5px;background:var(--white)}
.footer::after{content:"";position:absolute;left:0;right:0;bottom:0;height:3px;background:linear-gradient(90deg,var(--navy) 70%,var(--green) 70%)}
.brand-dot{width:9px;height:9px;border-radius:50%;background:var(--green);flex:none}
.brand-name{font-weight:700;font-size:6px;color:var(--navy);text-transform:uppercase;letter-spacing:.3px}
.footer .url{margin-left:auto;font-size:5px;color:var(--navy)}
.footer .num{font-size:5px;color:var(--white);background:var(--navy);border-radius:50%;width:10px;height:10px;display:flex;align-items:center;justify-content:center}
.photo{position:absolute;background:linear-gradient(135deg,#8fc0e8,#2f6fb0 60%,#1f3d7a)}
.photo-round{border-radius:50%}
.card{position:absolute;background:var(--white);border:1px solid #e3e6ef;border-radius:4px;box-shadow:0 2px 5px rgba(30,35,80,.08);padding:8px}
.icon-badge{width:18px;height:18px;border-radius:50%;background:var(--green);display:flex;align-items:center;justify-content:center;margin-bottom:5px}
.card h4{font-size:6px;font-weight:700;color:var(--navy);margin-bottom:3px;text-transform:uppercase}
.pill{position:absolute;left:200px;width:170px;height:17px;background:var(--pill);border-radius:9px;display:flex;align-items:center;font-size:6.5px;font-weight:700;color:var(--navy)}
.pill .n{width:17px;height:17px;border-radius:50%;background:var(--navy);color:var(--white);display:flex;align-items:center;justify-content:center;font-size:6px;margin-right:8px}
.pill:nth-of-type(even) .n{background:var(--green)}
.label{position:absolute;font-size:5.5px;font-weight:700;color:var(--navy);text-transform:uppercase;line-height:1.3}
.cover-brand{left:20px;top:22px;width:210px;display:flex;align-items:center;gap:7px}
.cover-brand .name{font-weight:800;font-size:11px;line-height:1.2;color:var(--navy)}
</style>
</head>
<body>

<!-- Cover -->
<section class="slide col-a row-1">
  <svg class="abs" style="left:0;top:0" width="400" height="225" viewBox="0 0 400 225">
    <path d="M0 190 C120 175 230 215 400 170 L400 225 L0 225Z" fill="var(--navy)"/>
    <path d="M0 186 C120 170 230 208 400 163" fill="none" stroke="var(--green)" stroke-width="4"/>
    <path d="M250 0 L400 0 L400 170 C340 150 270 120 250 0Z" fill="var(--navy)"/>
    <path d="M236 0 C252 110 320 150 400 162" fill="none" stroke="var(--green)" stroke-width="5"/>
  </svg>
  <div class="abs photo photo-round" style="left:262px;top:24px;width:118px;height:118px;border:4px solid var(--white)" role="img" aria-label="Doctors reviewing a scan together"></div>
  <div class="abs cover-brand">
    <span class="brand-dot" style="width:22px;height:22px;background:var(--navy)"></span>
    <span class="name">BRIGHTWELL<br>MEDICAL IMAGING</span>
  </div>
  <div class="abs" style="left:20px;top:72px;font-weight:800;font-size:18px;line-height:1.1;color:var(--navy)">PRECISION<br><span style="color:var(--green)">YOU CAN TRUST</span></div>
  <p class="abs body-copy" style="left:20px;top:120px;width:160px">Advanced diagnostic imaging with a focus on accuracy, comfort and care.</p>
</section>

<!-- Patient-centered care -->
<section class="slide col-b row-1">
  <h2 class="title">PATIENT-CENTERED CARE</h2>
  <div class="card" style="left:16px;top:42px;width:116px;height:72px">
    <div class="icon-badge"><svg width="10" height="10" viewBox="0 0 10 10"><path d="M2 5l2 2 4-4" stroke="#fff" stroke-width="1.5" fill="none"/></svg></div>
    <h4>Fast appointment scheduling</h4>
    <p class="body-copy">Book quickly and be seen within days, not weeks.</p>
  </div>
  <div class="card" style="left:142px;top:42px;width:116px;height:72px">
    <div class="icon-badge"><svg width="10" height="10" viewBox="0 0 10 10"><path d="M2 5l2 2 4-4" stroke="#fff" stroke-width="1.5" fill="none"/></svg></div>
    <h4>Ordering &amp; reporting online</h4>
    <p class="body-copy">Referrers send orders and get results in one place.</p>
  </div>
  <div class="card" style="left:268px;top:42px;width:116px;height:72px">
    <div class="icon-badge"><svg width="10" height="10" viewBox="0 0 10 10"><path d="M2 5l2 2 4-4" stroke="#fff" stroke-width="1.5" fill="none"/></svg></div>
    <h4>Accessible for patients of all ages</h4>
    <p class="body-copy">Calm rooms and caring staff for every visitor.</p>
  </div>
  <div class="abs" style="left:16px;top:124px;display:flex;gap:10px">
    <div style="width:116px"><span class="brand-dot" style="display:inline-block"></span><p class="body-copy">Clear guidance before and after each scan.</p></div>
    <div style="width:116px"><span class="brand-dot" style="display:inline-block"></span><p class="body-copy">Results shared quickly with your doctor.</p></div>
    <div style="width:116px"><span class="brand-dot" style="display:inline-block"></span><p class="body-copy">Flexible hours for busy families.</p></div>
  </div>
  <footer class="footer"><span class="brand-dot"></span><span class="brand-name">Brightwell Medical Imaging</span><span class="url">www.brightwellimaging.com</span><span class="num">2</span></footer>
</section>

<!-- Table of contents -->
<section class="slide col-a row-2">
  <h2 class="title">TABLE OF CONTENTS</h2>
  <div class="photo" style="left:16px;top:40px;width:160px;height:140px;border-radius:4px;background:linear-gradient(135deg,#bfe3c4,#3cb44b 55%,#2b2d6e)" role="img" aria-label="Glowing medical cross over a digital interface"></div>
  <div class="pill" style="top:42px"><span class="n">01</span>OUR SOLUTIONS</div>
  <div class="pill" style="top:68px"><span class="n">02</span>WHO WE ARE</div>
  <div class="pill" style="top:94px"><span class="n">03</span>VALUE PROPOSITION</div>
  <div class="pill" style="top:120px"><span class="n">04</span>KEY BENEFITS</div>
  <div class="pill" style="top:146px"><span class="n">05</span>MARKET OPPORTUNITY</div>
  <footer class="footer"><span class="brand-dot"></span><span class="brand-name">Brightwell Medical Imaging</span><span class="url">www.brightwellimaging.com</span><span class="num">3</span></footer>
</section>

<!-- Key benefits -->
<section class="slide col-b row-2">
  <h2 class="title">KEY BENEFITS</h2>
  <svg class="abs" style="left:40px;top:34px" width="150" height="150" viewBox="0 0 150 150">
    <circle cx="75" cy="75" r="70" fill="none" stroke="var(--green)" stroke-width="5" stroke-dasharray="300 140"/>
    <circle cx="75" cy="75" r="70" fill="none" stroke="var(--navy)" stroke-width="5" stroke-dasharray="0 300 140 0"/>
  </svg>
  <div class="photo photo-round" style="left:52px;top:46px;width:126px;height:126px" role="img" aria-label="Clinician holding a tablet showing scan results"></div>
  <div class="abs" style="left:215px;top:44px;width:170px">
    <div style="display:flex;gap:6px;margin-bottom:12px"><span class="brand-dot" style="width:14px;height:14px"></span><div><h4 style="font-size:6px;color:var(--navy)">THE POWER</h4><p class="body-copy">Modern scanners for sharper, faster images.</p></div></div>
    <div style="display:flex;gap:6px;margin-bottom:12px"><span class="brand-dot" style="width:14px;height:14px;background:var(--navy)"></span><div><h4 style="font-size:6px;color:var(--navy)">AN OUTSTANDING EXPERIENCE</h4><p class="body-copy">Comfort and clear care at every step.</p></div></div>
    <div style="display:flex;gap:6px"><span class="brand-dot" style="width:14px;height:14px;background:var(--blue)"></span><div><h4 style="font-size:6px;color:var(--navy)">AN OPERATING PLATFORM</h4><p class="body-copy">Connected systems that link every referrer.</p></div></div>
  </div>
  <footer class="footer"><span class="brand-dot"></span><span class="brand-name">Brightwell Medical Imaging</span><span class="url">www.brightwellimaging.com</span><span class="num">4</span></footer>
</section>

<!-- Who we are -->
<section class="slide col-a row-3">
  <h2 class="title">WHO WE ARE</h2>
  <div class="abs body-copy" style="left:16px;top:40px;width:180px">
    <p style="margin-bottom:6px">We are a modern imaging center built around accuracy, speed and the comfort of each patient who walks through our doors.</p>
    <p style="margin-bottom:6px">Our team of radiologists and technologists uses advanced equipment to deliver clear images and timely reports to referring physicians.</p>
    <p>We believe that great diagnostic care starts with listening, explaining each step and treating every patient with respect.</p>
  </div>
  <div class="photo" style="left:210px;top:0;width:190px;height:203px;background:linear-gradient(160deg,#9fd3f2,#2f7fc1 50%,#1f2157)" role="img" aria-label="Clinician touching a digital body scan display"></div>
  <footer class="footer"><span class="brand-dot"></span><span class="brand-name">Brightwell Medical Imaging</span><span class="url">www.brightwellimaging.com</span><span class="num">5</span></footer>
</section>

<!-- How it works -->
<section class="slide col-b row-3">
  <h2 class="title">HOW IT WORKS</h2>
  <svg class="abs" style="left:20px;top:70px" width="360" height="80" viewBox="0 0 360 80">
    <path d="M10 40 A30 30 0 0 1 70 40" fill="none" stroke="var(--navy)" stroke-width="7"/>
    <path d="M70 40 A30 30 0 0 0 130 40" fill="none" stroke="var(--green)" stroke-width="7"/>
    <path d="M130 40 A30 30 0 0 1 190 40" fill="none" stroke="var(--navy)" stroke-width="7"/>
    <path d="M190 40 A30 30 0 0 0 250 40" fill="none" stroke="var(--green)" stroke-width="7"/>
    <path d="M250 40 A30 30 0 0 1 310 40" fill="none" stroke="var(--navy)" stroke-width="7"/>
    <path d="M310 40 L345 40" stroke="var(--green)" stroke-width="7"/>
    <path d="M343 32 L355 40 L343 48Z" fill="var(--green)"/>
  </svg>
  <div class="label" style="left:18px;top:44px">Physician refers<br>the patient</div>
  <div class="label" style="left:140px;top:44px">Scan is booked</div>
  <div class="label" style="left:258px;top:44px">Images captured</div>
  <div class="label" style="left:80px;top:158px">Patient check-in</div>
  <div class="label" style="left:196px;top:158px">Radiologist reads</div>
  <div class="label" style="left:300px;top:158px">Report sent<br>to doctor</div>
  <footer class="footer"><span class="brand-dot"></span><span class="brand-name">Brightwell Medical Imaging</span><span class="url">www.brightwellimaging.com</span><span class="num">6</span></footer>
</section>

<!-- Imaging services -->
<section class="slide col-a row-4">
  <h2 class="title">OUR IMAGING SERVICES</h2>
  <svg class="abs" style="left:150px;top:50px" width="100" height="100" viewBox="0 0 100 100">
    <circle cx="50" cy="50" r="44" fill="none" stroke="var(--navy)" stroke-width="10" stroke-dasharray="70 68"/>
    <circle cx="50" cy="50" r="44" fill="none" stroke="var(--green)" stroke-width="10" stroke-dasharray="0 69 69 0"/>
    <circle cx="50" cy="50" r="22" fill="var(--blue)"/>
  </svg>
  <div class="label" style="left:160px;top:36px">Ultrasound</div>
  <div class="label" style="left:262px;top:68px">X-ray / digital<br>radiography</div>
  <div class="label" style="left:262px;top:124px">Additional<br>diagnostic services</div>
  <div class="label" style="left:50px;top:68px;text-align:right">CT scan /<br>computed tomography</div>
  <div class="label" style="left:50px;top:124px;text-align:right">MRI / magnetic<br>resonance imaging</div>
  <footer class="footer"><span class="brand-dot"></span><span class="brand-name">Brightwell Medical Imaging</span><span class="url">www.brightwellimaging.com</span><span class="num">7</span></footer>
</section>

<!-- Thank you -->
<section class="slide col-b row-4">
  <div class="abs" style="left:0;right:0;top:92px;text-align:center;font-weight:800;font-size:20px;color:var(--navy);letter-spacing:1px">THANK YOU</div>
  <footer class="footer"><span class="brand-dot"></span><span class="brand-name">Brightwell Medical Imaging</span><span class="url">www.brightwellimaging.com</span><span class="num">8</span></footer>
</section>

<!-- Our technology -->
<section class="slide col-a row-5">
  <h2 class="title">OUR TECHNOLOGY</h2>
  <div class="card" style="left:16px;top:42px;width:86px;height:112px;text-align:center">
    <div class="icon-badge" style="margin:0 auto 5px"></div><h4>High-definition equipment</h4><p class="body-copy">Latest scanners for clear detail.</p>
  </div>
  <div class="card" style="left:110px;top:42px;width:86px;height:112px;text-align:center">
    <div class="icon-badge" style="margin:0 auto 5px;background:var(--navy)"></div><h4>Reduced radiation dose</h4><p class="body-copy">Safer scans for every patient.</p>
  </div>
  <div class="card" style="left:204px;top:42px;width:86px;height:112px;text-align:center">
    <div class="icon-badge" style="margin:0 auto 5px"></div><h4>Secure digital archive</h4><p class="body-copy">Images stored and shared safely.</p>
  </div>
  <div class="card" style="left:298px;top:42px;width:86px;height:112px;text-align:center">
    <div class="icon-badge" style="margin:0 auto 5px;background:var(--navy)"></div><h4>Consistent image quality</h4><p class="body-copy">Checked daily by our team.</p>
  </div>
  <footer class="footer"><span class="brand-dot"></span><span class="brand-name">Brightwell Medical Imaging</span><span class="url">www.brightwellimaging.com</span><span class="num">9</span></footer>
</section>

<!-- Brand mark -->
<div class="abs" style="left:430px;top:1005px;width:370px;display:flex;align-items:center;gap:10px;justify-content:center">
  <span class="brand-dot" style="width:46px;height:46px;background:var(--navy)"></span>
  <span style="font-weight:800;font-size:20px;color:var(--navy);line-height:1.15">BRIGHTWELL<br>MEDICAL IMAGING</span>
</div>

</body>
</html>
```